New Townhome community needs for sale sign.

need a 4 foot by 8 foot banner to put on building listing newly constructed townhomes as "coming soon" to market. Construction is scheduled to be completed Dec 2024. Sale of units will begin Spring of 2025.
6 individual townhome units each 2,000 square feet. each unit is 3 bedroom 2.5 bathroom with 2 car garage and each has a rooftop "sky lounge" with amazing views. Gated community. Units available for sale Spring of 2025. Real estate company selling units will be KTL & Associates. Will need KTL & Associates Logo on the banner. Would like to keep with the same blue color scheme as the KTL & Associates logo. phone number on banner to be 480-555-3164. web ktlpartners.example.

```html
<!DOCTYPE html>
<html lang="en">
<head>
<meta charset="utf-8">
<title>KTL &amp; Associates — Townhomes Coming Soon</title>
<link rel="stylesheet" href="https://fonts.googleapis.com/css2?family=Montserrat:ital,wght@0,500;0,600;0,700;0,800;1,500;1,800&display=swap">
<style>
  :root {
    --brand-blue: #2a9fd3;
    --brand-blue-deep: #238cc0;
    --ink-navy: #1d2b4a;
    --ink-dark: #222;
    --paper: #ffffff;
    --paper-shade: #eef0f2;
    --dot-light: #7cc4e6;
    --dot-dark: #b4bac1;
  }
  * { box-sizing: border-box; margin: 0; padding: 0; }
  html, body { width: 1200px; height: 723px; overflow: hidden; background: var(--paper); }
  .banner {
    position: relative;
    width: 1200px;
    height: 723px;
    overflow: hidden;
    background: linear-gradient(180deg, var(--paper) 0%, var(--paper-shade) 100%);
    font-family: "Montserrat", sans-serif;
    color: var(--ink-dark);
  }
  .side-panel {
    position: absolute; left: 0; top: 0;
    width: 295px; height: 723px;
    background: var(--brand-blue);
  }
  .dot-field-top {
    position: absolute; left: 38px; top: 65px;
    width: 120px; height: 120px;
    background: var(--dot-light); opacity: .3;
  }
  .cross-marks {
    position: absolute; left: 384px; top: 32px;
    width: 72px; height: 4px;
    background: var(--ink-dark); opacity: .45;
  }
  .hero-photo {
    position: absolute; left: 60px; top: 105px;
    width: 360px; height: 520px;
    background: radial-gradient(ellipse at 50% 35%, #ecebe8 0%, #c3c5c8 55%, #8f949b 100%);
  }
  .accent-square {
    position: absolute; left: 392px; top: 543px;
    width: 103px; height: 98px;
    background: var(--brand-blue-deep);
  }
  .dot-field-bottom {
    position: absolute; left: 348px; top: 664px;
    width: 86px; height: 30px;
    background: var(--dot-dark); opacity: .4;
  }
  .brand {
    position: absolute; right: 104px; top: 62px;
    display: flex; align-items: center; gap: 10px;
    font-weight: 600; font-size: 26px; color: var(--ink-navy);
    white-space: nowrap;
  }
  .brand-mark { width: 24px; height: 24px; background: var(--brand-blue); }
  .headline {
    position: absolute; right: 108px; top: 150px;
    font-weight: 800; font-size: 85px; line-height: 1;
    color: var(--brand-blue); letter-spacing: -1px;
    white-space: nowrap;
  }
  .launch-line {
    position: absolute; right: 108px; top: 250px;
    font-size: 32px; color: var(--brand-blue-deep);
    white-space: nowrap;
  }
  .launch-line .lead { font-style: italic; font-weight: 500; margin-right: 18px; }
  .launch-line .date { font-style: italic; font-weight: 800; }
  .divider {
    position: absolute; left: 628px; top: 330px;
    width: 572px; height: 2px; background: var(--ink-dark);
  }
  .unit-summary {
    position: absolute; right: 108px; top: 358px;
    text-align: right;
  }
  .unit-summary h2 { font-weight: 700; font-size: 25px; color: var(--ink-dark); margin-bottom: 10px; white-space: nowrap; }
  .unit-summary ul { list-style: none; }
  .unit-summary li { font-weight: 500; font-size: 18px; line-height: 36px; color: var(--ink-dark); white-space: nowrap; }
  .contact-band {
    position: absolute; left: 495px; top: 641px;
    width: 705px; height: 82px;
    background: var(--brand-blue);
    display: flex; align-items: center; gap: 30px;
    padding-left: 50px;
    color: var(--paper); font-weight: 600; font-size: 28px;
    white-space: nowrap;
  }
</style>
</head>
<body>
  <main class="banner">
    <div class="side-panel"></div>
    <div class="dot-field-top" role="img" aria-label="Grid of small white dots"></div>
    <div class="cross-marks" role="img" aria-label="Row of small plus marks"></div>
    <div class="hero-photo" role="img" aria-label="Photo of a hand in a suit sleeve holding a model house"></div>
    <div class="accent-square"></div>
    <div class="dot-field-bottom" role="img" aria-label="Grid of small grey dots"></div>

    <div class="brand"><span class="brand-mark"></span><span>KTL &amp; Associates</span></div>

    <h1 class="headline">COMING SOON</h1>
    <p class="launch-line"><span class="lead">Units Sale</span><span class="date">Spring 2025</span></p>
    <div class="divider"></div>

    <section class="unit-summary">
      <h2>6 Individual Townhome Units</h2>
      <ul>
        <li>2,000 Square Feet</li>
        <li>3 Bedroom</li>
        <li>2.5 Bathroom With</li>
        <li>2 Car Garage Rooftop "Sky Lounge"</li>
        <li>Gated Community</li>
      </ul>
    </section>

    <footer class="contact-band">
      <span class="phone">480-555-3164</span>
      <span class="web">www.ktlpartners.example</span>
    </footer>
  </main>
</body>
</html>
```